The Harborline LLC Asset Classes

I'm looking for for two designs here to go into powerpoint and potentially as a standalone PDF. My company does wealth management.
Graphic Image #1
I break down the investment world into 4 broad categories
-Preservation
-Capital Markets
-Real Estate
-Alternatives
In each broad category, there are subcategories:
Preservation: cash, checking/savings accounts, money market accounts, CD's, and fixed annuities.
Capital Markets: Publicly traded stocks and bonds
Real Estate: single-family residence, retail, industrial, multifamily, and office
Alternatives: private equity, private credit, cryptocurrency, asset-backed loans, tax liens, oil & gas, litigation finance, and royalties
Graphic 2: Please see the bottom f page 1 of the Tidewater Slides PDF.
Just like in graphic one, you have 4 categories of the Capital Markets and their respective subcategories
Category 1: Domestic Stocks: Subcategories are Large, mid, and small size companies
Category 2: International Stocks: Subcategories are Large, Mid/Small and by region - Developed and Emerging
Category 3: Fixed Income: You have subcategories like corporate, municipal, government, domestic, international
Category 4: Alternatives: The subcategories are metals and real estate
---------------------
I'm looking to create a graphic (either pie chart, or a circle broken into parts or some other clever way to illustrate this) to clearly illustrate both of these universes in a clean, professional, slick manner.
Target Market(s)
Investors
Colors
Designer to choose colors to be used in the design.
Requirements
Must have
- Clean
- professional
- Easy to read
- Creative
- Visually appealling
Nice to have
- I have attached my logo and some marketing materials so you can get a feel of what I am doing. Maybe you can clean this up too!

```html
<!DOCTYPE html>
<html lang="en">
<head>
<meta charset="utf-8">
<title>The Harborline LLC — Asset Classes</title>
<link rel="stylesheet" href="https://fonts.googleapis.com/css2?family=Lato:wght@400;700;900&display=swap">
<style>
  :root {
    --ink: #1f1f1f;
    --brand-blue: #1f6b94;
    --brand-orange: #e38a2a;
    --panel-cool: #eef3f6;
    --panel-warm: #fcf6ee;
    --navy-1: #8fbac4;
    --navy-2: #5d8aa0;
    --navy-3: #2f5566;
    --navy-4: #1f3a4c;
    --navy-5: #12262f;
    --sky-1: #9dd0dd;
    --sky-2: #236e96;
    --alt-1: #236a92;
    --alt-2: #2e7eaa;
    --alt-3: #3f90c2;
    --alt-4: #4a9cc9;
    --alt-5: #5db6db;
    --alt-6: #6ccbdc;
    --alt-7: #9ed0dc;
    --alt-8: #bdd3dd;
    --sand-1: #d8c8aa;
    --sand-2: #cfae7f;
    --sand-3: #a67c4a;
    --sand-4: #8f602d;
    --sand-5: #834d18;
    --amber-1: #edb274;
    --amber-2: #e38a2a;
    --brown-ring: #7b4614;
    --tan-ring: #a8865f;
  }
  html, body { margin: 0; padding: 0; width: 960px; height: 1200px; overflow: hidden; background: #fff; }
  .sheet { display: block; width: 960px; height: 1200px; font-family: "Lato", sans-serif; }
  .title { font-family: "Lato", sans-serif; font-weight: 700; font-size: 37px; text-anchor: end; }
  .title--accent { fill: var(--brand-blue); }
  .title--dark { fill: #111; }
  .title-rule { fill: var(--brand-orange); }
  .label { font-family: "Lato", sans-serif; font-size: 13.5px; fill: var(--ink); }
  .label--mid { text-anchor: middle; }
  .label--end { text-anchor: end; }
  .hub { font-family: "Lato", sans-serif; font-weight: 900; font-size: 12.5px; text-anchor: middle; letter-spacing: 0.2px; }
  .hub--dark { fill: #111; }
  .hub--blue { fill: var(--brand-blue); }
  .seg { fill: none; stroke-width: 115; }
  .seg--markets { stroke-width: 103; }
  .ring { fill: none; stroke-width: 13; }
  .ring--markets { stroke-width: 12; }
  .divider-cool { stroke: #0c1a22; stroke-width: 1.5; }
  .divider-warm { stroke: #6f3f12; stroke-width: 1.5; }
  .brand-name { font-family: "Lato", sans-serif; font-weight: 700; font-size: 22px; fill: var(--brand-blue); }
</style>
</head>
<body>
<svg class="sheet" viewBox="0 0 1275 1594" xmlns="http://www.w3.org/2000/svg">

  <!-- Section heading: wealth management -->
  <text class="title title--accent" x="300" y="249">WEALTH</text>
  <text class="title title--dark" x="300" y="285">MANAGEMENT</text>
  <rect class="title-rule" x="40" y="315" width="260" height="7"/>

  <!-- Wealth management wheel -->
  <g class="wheel wheel--wealth">
    <polygon fill="var(--panel-cool)" points="607,75 969,75 969,210 787,392 607,210"/>
    <polygon fill="var(--panel-cool)" points="378,221 588,221 773,406 588,591 378,591"/>
    <polygon fill="var(--panel-cool)" points="1195,221 986,221 801,406 986,591 1195,591"/>
    <polygon fill="var(--panel-cool)" points="607,737 969,737 969,602 787,420 607,602"/>

    <g transform="translate(787 406)">
      <!-- Preservation -->
      <circle class="seg" r="182.5" pathLength="360" stroke="var(--navy-1)" stroke-dasharray="17 360" transform="rotate(227.5)"/>
      <circle class="seg" r="182.5" pathLength="360" stroke="var(--navy-2)" stroke-dasharray="17 360" transform="rotate(244.5)"/>
      <circle class="seg" r="182.5" pathLength="360" stroke="var(--navy-3)" stroke-dasharray="17 360" transform="rotate(261.5)"/>
      <circle class="seg" r="182.5" pathLength="360" stroke="var(--navy-4)" stroke-dasharray="17 360" transform="rotate(278.5)"/>
      <circle class="seg" r="182.5" pathLength="360" stroke="var(--navy-5)" stroke-dasharray="17 360" transform="rotate(295.5)"/>
      <!-- Capital markets -->
      <circle class="seg" r="182.5" pathLength="360" stroke="var(--sky-1)" stroke-dasharray="42.5 360" transform="rotate(-42.5)"/>
      <circle class="seg" r="182.5" pathLength="360" stroke="var(--sky-2)" stroke-dasharray="42.5 360" transform="rotate(0)"/>
      <!-- Real estate -->
      <circle class="seg" r="182.5" pathLength="360" stroke="var(--navy-1)" stroke-dasharray="17 360" transform="rotate(47.5)"/>
      <circle class="seg" r="182.5" pathLength="360" stroke="var(--navy-2)" stroke-dasharray="17 360" transform="rotate(64.5)"/>
      <circle class="seg" r="182.5" pathLength="360" stroke="var(--navy-3)" stroke-dasharray="17 360" transform="rotate(81.5)"/>
      <circle class="seg" r="182.5" pathLength="360" stroke="var(--navy-4)" stroke-dasharray="17 360" transform="rotate(98.5)"/>
      <circle class="seg" r="182.5" pathLength="360" stroke="var(--navy-5)" stroke-dasharray="17 360" transform="rotate(115.5)"/>
      <!-- Alternatives -->
      <circle class="seg" r="182.5" pathLength="360" stroke="var(--alt-8)" stroke-dasharray="10.625 360" transform="rotate(137.5)"/>
      <circle class="seg" r="182.5" pathLength="360" stroke="var(--alt-7)" stroke-dasharray="10.625 360" transform="rotate(148.125)"/>
      <circle class="seg" r="182.5" pathLength="360" stroke="var(--alt-6)" stroke-dasharray="10.625 360" transform="rotate(158.75)"/>
      <circle class="seg" r="182.5" pathLength="360" stroke="var(--alt-5)" stroke-dasharray="10.625 360" transform="rotate(169.375)"/>
      <circle class="seg" r="182.5" pathLength="360" stroke="var(--alt-4)" stroke-dasharray="10.625 360" transform="rotate(180)"/>
      <circle class="seg" r="182.5" pathLength="360" stroke="var(--alt-3)" stroke-dasharray="10.625 360" transform="rotate(190.625)"/>
      <circle class="seg" r="182.5" pathLength="360" stroke="var(--alt-2)" stroke-dasharray="10.625 360" transform="rotate(201.25)"/>
      <circle class="seg" r="182.5" pathLength="360" stroke="var(--alt-1)" stroke-dasharray="10.625 360" transform="rotate(211.875)"/>

      <g class="divider-cool">
        <line x1="125" x2="240" transform="rotate(244.5)"/>
        <line x1="125" x2="240" transform="rotate(261.5)"/>
        <line x1="125" x2="240" transform="rotate(278.5)"/>
        <line x1="125" x2="240" transform="rotate(295.5)"/>
        <line x1="125" x2="240" transform="rotate(0)"/>
        <line x1="125" x2="240" transform="rotate(64.5)"/>
        <line x1="125" x2="240" transform="rotate(81.5)"/>
        <line x1="125" x2="240" transform="rotate(98.5)"/>
        <line x1="125" x2="240" transform="rotate(115.5)"/>
        <line x1="125" x2="240" transform="rotate(148.125)"/>
        <line x1="125" x2="240" transform="rotate(158.75)"/>
        <line x1="125" x2="240" transform="rotate(169.375)"/>
        <line x1="125" x2="240" transform="rotate(180)"/>
        <line x1="125" x2="240" transform="rotate(190.625)"/>
        <line x1="125" x2="240" transform="rotate(201.25)"/>
        <line x1="125" x2="240" transform="rotate(211.875)"/>
      </g>

      <!-- Category rings -->
      <circle class="ring" r="118.5" pathLength="360" stroke="var(--navy-5)" stroke-dasharray="85 360" transform="rotate(227.5)"/>
      <circle class="ring" r="118.5" pathLength="360" stroke="var(--alt-1)" stroke-dasharray="85 360" transform="rotate(-42.5)"/>
      <circle class="ring" r="118.5" pathLength="360" stroke="var(--navy-5)" stroke-dasharray="85 360" transform="rotate(47.5)"/>
      <circle class="ring" r="118.5" pathLength="360" stroke="var(--alt-1)" stroke-dasharray="85 360" transform="rotate(137.5)"/>

      <circle r="110" fill="#fff" stroke="var(--brand-orange)" stroke-width="4"/>
      <g fill="#3b4850">
        <polygon points="0,0 130,-4 130,4" transform="rotate(45)"/>
        <polygon points="0,0 130,-4 130,4" transform="rotate(135)"/>
        <polygon points="0,0 130,-4 130,4" transform="rotate(225)"/>
        <polygon points="0,0 130,-4 130,4" transform="rotate(315)"/>
      </g>
    </g>

    <text class="hub hub--dark" x="787" y="337">PRESERVATION</text>
    <text class="hub hub--dark" x="729" y="411">ALTERNATIVES</text>
    <text class="hub hub--dark" x="852" y="404">CAPITAL</text>
    <text class="hub hub--dark" x="852" y="417">MARKETS</text>
    <text class="hub hub--dark" x="787" y="486">REAL ESTATE</text>

    <text class="label" x="616" y="177">Cash</text>
    <text class="label" x="626" y="134">Savings accounts</text>
    <text class="label label--mid" x="787" y="113">Money market</text>
    <text class="label label--mid" x="787" y="127">accounts</text>
    <text class="label" x="847" y="136">CD's</text>
    <text class="label" x="901" y="156">Fixed</text>
    <text class="label" x="901" y="170">annuities</text>
    <text class="label" x="1047" y="320">Publicly traded</text>
    <text class="label" x="1047" y="334">stocks</text>
    <text class="label" x="1045" y="497">Bonds</text>
    <text class="label" x="621" y="654">Office</text>
    <text class="label" x="665" y="678">Multifamily</text>
    <text class="label" x="758" y="692">Industrial</text>
    <text class="label" x="834" y="678">Retail</text>
    <text class="label" x="881" y="658">Single-family</text>
    <text class="label" x="881" y="672">residence</text>
    <text class="label" x="481" y="262">Private equity</text>
    <text class="label" x="458" y="296">Private credit</text>
    <text class="label" x="424" y="337">Cryptocurrency</text>
    <text class="label label--end" x="511" y="381">Asset-backed</text>
    <text class="label label--end" x="511" y="395">loans</text>
    <text class="label" x="458" y="436">Tax liens</text>
    <text class="label" x="468" y="480">Oil &amp; gas</text>
    <text class="label" x="435" y="519">Litigation finance</text>
    <text class="label" x="510" y="556">Royalties</text>
  </g>

  <!-- Section heading: capital markets -->
  <text class="title title--accent" x="300" y="1026">CAPITAL</text>
  <text class="title title--dark" x="300" y="1062">MARKETS</text>
  <rect class="title-rule" x="130" y="1092" width="170" height="7"/>

  <!-- Capital markets wheel -->
  <g class="wheel wheel--markets">
    <polygon fill="var(--panel-warm)" points="607,853 969,853 969,987 787,1169 607,987"/>
    <polygon fill="var(--panel-warm)" points="378,999 589,999 773,1183 589,1367 378,1367"/>
    <polygon fill="var(--panel-warm)" points="1195,999 985,999 801,1183 985,1367 1195,1367"/>
    <polygon fill="var(--panel-warm)" points="607,1514 969,1514 969,1379 787,1197 607,1379"/>

    <g transform="translate(787 1183)">
      <!-- Domestic stocks -->
      <circle class="seg seg--markets" r="188.5" pathLength="360" stroke="var(--sand-1)" stroke-dasharray="28.333 360" transform="rotate(227.5)"/>
      <circle class="seg seg--markets" r="188.5" pathLength="360" stroke="var(--sand-3)" stroke-dasharray="28.333 360" transform="rotate(255.833)"/>
      <circle class="seg seg--markets" r="188.5" pathLength="360" stroke="var(--sand-5)" stroke-dasharray="28.333 360" transform="rotate(284.167)"/>
      <!-- International stocks -->
      <circle class="seg seg--markets" r="188.5" pathLength="360" stroke="var(--amber-1)" stroke-dasharray="42.5 360" transform="rotate(-42.5)"/>
      <circle class="seg seg--markets" r="188.5" pathLength="360" stroke="var(--amber-2)" stroke-dasharray="42.5 360" transform="rotate(0)"/>
      <!-- Fixed income -->
      <circle class="seg seg--markets" r="188.5" pathLength="360" stroke="var(--sand-1)" stroke-dasharray="17 360" transform="rotate(47.5)"/>
      <circle class="seg seg--markets" r="188.5" pathLength="360" stroke="var(--sand-2)" stroke-dasharray="17 360" transform="rotate(64.5)"/>
      <circle class="seg seg--markets" r="188.5" pathLength="360" stroke="var(--sand-3)" stroke-dasharray="17 360" transform="rotate(81.5)"/>
      <circle class="seg seg--markets" r="188.5" pathLength="360" stroke="var(--sand-4)" stroke-dasharray="17 360" transform="rotate(98.5)"/>
      <circle class="seg seg--markets" r="188.5" pathLength="360" stroke="var(--sand-5)" stroke-dasharray="17 360" transform="rotate(115.5)"/>
      <!-- Alternatives -->
      <circle class="seg seg--markets" r="188.5" pathLength="360" stroke="var(--amber-1)" stroke-dasharray="42.5 360" transform="rotate(137.5)"/>
      <circle class="seg seg--markets" r="188.5" pathLength="360" stroke="var(--amber-2)" stroke-dasharray="42.5 360" transform="rotate(180)"/>

      <g class="divider-warm">
        <line x1="137" x2="240" transform="rotate(255.833)"/>
        <line x1="137" x2="240" transform="rotate(284.167)"/>
        <line x1="137" x2="240" transform="rotate(64.5)"/>
        <line x1="137" x2="240" transform="rotate(81.5)"/>
        <line x1="137" x2="240" transform="rotate(98.5)"/>
        <line x1="137" x2="240" transform="rotate(115.5)"/>
      </g>

      <circle class="ring ring--markets" r="131" pathLength="360" stroke="var(--brown-ring)" stroke-dasharray="85 360" transform="rotate(227.5)"/>
      <circle class="ring ring--markets" r="131" pathLength="360" stroke="var(--tan-ring)" stroke-dasharray="85 360" transform="rotate(-42.5)"/>
      <circle class="ring ring--markets" r="131" pathLength="360" stroke="var(--brown-ring)" stroke-dasharray="85 360" transform="rotate(47.5)"/>
      <circle class="ring ring--markets" r="131" pathLength="360" stroke="var(--tan-ring)" stroke-dasharray="85 360" transform="rotate(137.5)"/>

      <circle r="122" fill="#fff" stroke="var(--brown-ring)" stroke-width="4"/>
      <g fill="var(--brown-ring)">
        <polygon points="0,0 142,-4 142,4" transform="rotate(45)"/>
        <polygon points="0,0 142,-4 142,4" transform="rotate(135)"/>
        <polygon points="0,0 142,-4 142,4" transform="rotate(225)"/>
        <polygon points="0,0 142,-4 142,4" transform="rotate(315)"/>
      </g>
    </g>

    <text class="hub hub--blue" x="788" y="1100">DOMESTIC STOCKS</text>
    <text class="hub hub--blue" x="713" y="1188">ALTERNATIVES</text>
    <text class="hub hub--blue" x="857" y="1181">INTERNATIONAL</text>
    <text class="hub hub--blue" x="857" y="1194">STOCKS</text>
    <text class="hub hub--blue" x="787" y="1286">FIXED INCOME</text>

    <text class="label" x="624" y="924">Large size</text>
    <text class="label" x="624" y="938">companies</text>
    <text class="label label--mid" x="785" y="892">Mid size</text>
    <text class="label label--mid" x="785" y="906">companies</text>
    <text class="label" x="881" y="924">Small size</text>
    <text class="label" x="881" y="938">companies</text>
    <text class="label" x="1047" y="1117">Developed</text>
    <text class="label" x="1045" y="1274">Emerging</text>
    <text class="label" x="450" y="1120">Real estate</text>
    <text class="label" x="474" y="1259">Metals</text>
    <text class="label" x="615" y="1445">International</text>
    <text class="label" x="676" y="1470">Domestic</text>
    <text class="label" x="749" y="1484">Government</text>
    <text class="label" x="842" y="1469">Municipal</text>
    <text class="label" x="899" y="1445">Corporate</text>
  </g>

  <!-- Company name -->
  <g class="brand">
    <circle cx="112" cy="1546" r="9" fill="var(--brand-orange)"/>
    <text class="brand-name" x="128" y="1554">The Harborline LLC</text>
  </g>
</svg>
</body>
</html>
```